Civil Engineering Business Card Design

We need a business card design for an Civil Engineering Company located in Naples, Florida. The company name is Morrow Engineering.
What we do:
Site Evaluation
Review existing site conditions and zoning
Evaluation of potential development options
Evaluation of environmental permitting challenges
Prepare alternative master site development or redevelopment plan
Calculate cost and time lines for site development
Address political, environmental, social, and economic impacts of site development
Site Design
Prepare master site development plans
Zoning, rezoning, and zoning amendments for land use changes
Evaluate zoning and environmental permitting challenges
Value engineer alternative land development design and products
Residential Development
Plat development and design
Homeowner association document development
Single family development ranging from affordable housing to large estate projects
Multi family development ranging from duplexes to large scale condominiums
Amenity facilities such as golf courses, parks and clubhouse sites
Commercial Development
Office site and park designs development plans
Industrial site and park development plans
Shopping center site development design
Hospital site design development
Institutional Development
School design development and redevelopment plans
Park design development and enhancement plans
Downtown redevelopment plans for new and existing structures
Theater and park plan development
Parking garage design development
Governmental administration building design
Design Services
Site development
Environmental assessment
Roadway alignment and development
Surface water management
Drainage design
Water distribution system
Fire service analysis
Sewage collection systems
Sewage pump station and force main design
Cable utility conduit layout
Construction details
Construction documents
Technical specifications
Alternative methods and materials analysis
Services During Construction
Development of bid documents
Solicitation and processing of bids
Cost review and analysis
Construction cost estimating
Onsite construction observation
Coordination of field modifications to address unforeseen site conditions
Assess value engineering design and contract work
Review of pay requests and shop drawings
Review of warranties
Development assessment of onsite and offsite mitigation
Verification of construction completion, close out, and certification
Processing final pay requests and turn over
We want a clean design on a white background. We have a current logo but are not happy with it so changes would be greatly appreciated.
Industry/Entity Type
Construction
Contact Information for Business Card
Morrow Engineering
Creative Engineering Solutions Through Integrity and Experience
Leonard Morrow, President
4870 Bellwood Parkway East
Suite 417C
Naples, FL 30917
555-364-1905-Office, 555-490-6172-Mobile
Leo@MorrowEng.example, www.MorrowEng.example

```html
<!DOCTYPE html>
<html lang="en">
<head>
<meta charset="utf-8">
<title>Morrow Engineering – Business Card</title>
<link rel="stylesheet" href="https://fonts.googleapis.com/css2?family=Open+Sans:wght@400;600;700&display=swap">
<style>
  :root {
    --teal: #2fc6bf;
    --teal-dark: #22aea8;
    --navy: #3b3f9e;
    --ink: #4a4d55;
    --ink-soft: #6b6e76;
    --paper: #ffffff;
    --backdrop: #e9eaec;
  }
  * { box-sizing: border-box; margin: 0; padding: 0; }
  html, body { width: 1200px; height: 1023px; overflow: hidden; }
  body {
    background: var(--backdrop);
    font-family: "Open Sans", Arial, sans-serif;
    color: var(--ink);
    position: relative;
  }
  .card {
    position: absolute;
    left: 75px; top: 211px;
    width: 1050px; height: 600px;
    background: linear-gradient(135deg, #ffffff 0%, #f4f5f6 100%);
    box-shadow: 0 6px 24px rgba(0,0,0,.12);
    overflow: hidden;
  }
  .card-shapes { position: absolute; inset: 0; }
  .brand {
    position: absolute; left: 70px; top: 200px;
    display: flex; align-items: center; gap: 22px;
  }
  .brand-square { width: 64px; height: 64px; background: var(--navy); flex: none; }
  .brand-name {
    color: var(--navy); font-weight: 600; font-size: 46px;
    line-height: 1.05; text-transform: uppercase; letter-spacing: 2px;
  }
  .contact { position: absolute; left: 70px; top: 370px; font-size: 22px; color: var(--ink-soft); }
  .contact-row { display: flex; align-items: center; gap: 14px; height: 34px; }
  .contact-icon { width: 22px; height: 22px; flex: none; }
  .address { margin-top: 22px; text-transform: uppercase; font-size: 21px; line-height: 1.5; }
  .title-block {
    position: absolute; left: 575px; top: 66px; width: 430px;
    color: #fff; text-align: center;
  }
  .person-name {
    font-weight: 700; font-size: 34px; line-height: 1.2;
    text-transform: uppercase; letter-spacing: 1px; white-space: nowrap;
  }
  .person-role { font-size: 18px; letter-spacing: 3px; text-transform: uppercase; margin-top: 6px; }
  .services { position: absolute; left: 672px; top: 242px; list-style: none; font-size: 23px; color: var(--ink); }
  .services li { display: flex; align-items: center; gap: 14px; height: 40px; white-space: nowrap; }
  .services li::before { content: ""; width: 9px; height: 9px; border-radius: 50%; background: var(--teal); flex: none; }
</style>
</head>
<body>
  <section class="card">
    <svg class="card-shapes" width="1050" height="600" viewBox="0 0 1050 600" aria-hidden="true">
      <path fill="var(--teal)" d="M488 36 H1005 V205 H640 V515 L600 560 H575 V110 H488 Z"/>
      <path fill="var(--teal-dark)" d="M880 0 H1050 V150 H1040 V130 L1030 120 V14 H900 L890 10 H880 Z"/>
    </svg>

    <div class="brand">
      <div class="brand-square"></div>
      <div class="brand-name">Morrow<br>Engineering</div>
    </div>

    <div class="contact">
      <div class="contact-row">
        <svg class="contact-icon" viewBox="0 0 22 22"><rect width="22" height="22" rx="3" fill="var(--navy)"/><path d="M7 5c1 0 2 3 1.5 4S8 11 11 14s3 1 4 .5 4 .5 4 1.5-2 2-3 2C10 18 4 12 4 8c0-1 2-3 3-3z" fill="#fff"/></svg>
        <span>555-364-1905</span>
      </div>
      <div class="contact-row">
        <svg class="contact-icon" viewBox="0 0 22 22"><rect width="22" height="22" rx="3" fill="var(--navy)"/><rect x="7" y="4" width="8" height="14" rx="1.5" fill="none" stroke="#fff" stroke-width="1.6"/><circle cx="11" cy="15.5" r="1" fill="#fff"/></svg>
        <span>555-490-6172</span>
      </div>
      <div class="contact-row">
        <svg class="contact-icon" viewBox="0 0 22 22"><rect width="22" height="22" rx="3" fill="var(--navy)"/><rect x="4" y="6" width="14" height="10" fill="none" stroke="#fff" stroke-width="1.5"/><path d="M4 6l7 6 7-6" fill="none" stroke="#fff" stroke-width="1.5"/></svg>
        <span>Leo@MorrowEng.example</span>
      </div>
      <div class="contact-row">
        <svg class="contact-icon" viewBox="0 0 22 22"><rect width="22" height="22" rx="3" fill="var(--navy)"/><circle cx="11" cy="11" r="6.5" fill="none" stroke="#fff" stroke-width="1.4"/><path d="M4.5 11h13M11 4.5c-3 3.5-3 9.5 0 13M11 4.5c3 3.5 3 9.5 0 13" fill="none" stroke="#fff" stroke-width="1.2"/></svg>
        <span>www.MorrowEng.example</span>
      </div>
      <p class="address">4870 Bellwood Parkway East<br>Suite 417C Naples, FL 30917</p>
    </div>

    <div class="title-block">
      <h1 class="person-name">Leonard Morrow</h1>
      <p class="person-role">President</p>
    </div>

    <ul class="services">
      <li>Site Evaluation</li>
      <li>Site Design</li>
      <li>Residential Development</li>
      <li>Commercial Development</li>
      <li>Institutional Development</li>
      <li>Design Services</li>
      <li>Services During Construction</li>
    </ul>
  </section>
</body>
</html>
```